Upsell Vertical Banner Ad Design For B2B Marketing Agency Vertical 768px × 1180px IS THE SIZE

I need a banner made for my website www.brightlanepromotionhub.biz This banner will be an upsell advertisement for after someone signs up for my monthly program. When they login to their account for the 1st time I will give them the chance to upgrade their account to our annual program with just one click.

this is a page that upsells it currently to give you an idea how we market ourselves:
https://tlpx.pagevault-example.com/page/tlp-annual-upsell

Use this content:

Are You Ready To Commit To Taking Your Business To The Next Level?

Because We're In This For The Long-Haul and Dedicated To Your Success...

Save $300 By Upgrading To An Annual Membership And Pay Only $74/mth

((BUTTON))Yes, Upgrade My Plan Right Now!

*Must prepay the full year at only $898/yr!

Target Market(s)

business owners

Industry/Entity Type

Marketing

Requirements
Must have
• 768px × 1180px IS THE SIZE vertical

Use this content:

Nice to have
• Use this content:

Should not have
• Use this content:

```html
<!DOCTYPE html>
<html lang="en">
<head>
<meta charset="utf-8">
<title>Annual Upgrade Offer – Bright Lane Promotion Hub</title>
<link href="https://fonts.googleapis.com/css2?family=Roboto:wght@300&family=Teko:wght@500;600&family=Ubuntu:wght@400;500&display=swap" rel="stylesheet">
<style>
  :root {
    --cream: #f3f4e8;
    --cream-light: #f8f8f0;
    --stone: #d9d9d2;
    --leaf: #78c142;
    --leaf-deep: #3f8f2a;
    --ink: #141414;
    --slate: #6b6c70;
    --ring: #c4c5c9;
    --button-top: #2fb556;
    --button-bottom: #12994a;
    --white: #ffffff;
  }
  * { margin: 0; padding: 0; box-sizing: border-box; }
  html, body { width: 781px; height: 1200px; overflow: hidden; background: var(--cream); }
  .banner { position: relative; width: 781px; height: 1200px; overflow: hidden; }

  .hero-photo {
    position: absolute; inset: 0;
    background:
      radial-gradient(ellipse 260px 300px at 300px 620px, rgba(120,193,66,0.55), rgba(120,193,66,0) 70%),
      radial-gradient(ellipse 120px 260px at 560px 450px, rgba(120,193,66,0.45), rgba(120,193,66,0) 70%),
      radial-gradient(ellipse 190px 230px at 290px 960px, rgba(255,255,255,0.9), rgba(255,255,255,0) 75%),
      linear-gradient(180deg, var(--cream-light) 0%, var(--cream) 60%, var(--stone) 100%);
  }

  .headline { position: absolute; left: 32px; top: 38px; }
  .lead {
    font-family: "Roboto", sans-serif; font-weight: 300; color: var(--ink);
    font-size: 30px; line-height: 1;
  }
  .lead-question { position: absolute; left: 32px; top: 158px; font-size: 37px; }
  .lead-commit { position: absolute; left: 35px; top: 214px; font-size: 29px; line-height: 34px; }
  .display {
    position: absolute; font-family: "Teko", sans-serif; font-weight: 600;
    color: var(--leaf); line-height: 1; white-space: nowrap;
  }
  .display-business { left: 32px; top: 88px; font-size: 74px; letter-spacing: 1px; }
  .display-success { left: 36px; top: 288px; font-size: 78px; font-variant: small-caps; letter-spacing: 1px; }

  .offer-disc { position: absolute; left: 0; top: 0; }
  .offer {
    position: absolute; left: 555px; width: 220px; top: 603px; text-align: center;
    font-family: "Ubuntu", sans-serif;
  }
  .offer-save { color: var(--leaf); font-weight: 500; font-size: 28px; line-height: 34px; }
  .offer-terms { color: var(--white); font-size: 19.5px; line-height: 26.5px; margin-top: 2px; }
  .offer-price {
    font-family: "Teko", sans-serif; font-weight: 600; color: var(--leaf);
    font-size: 56px; line-height: 50px; font-variant: small-caps; margin-top: 8px;
  }

  .upgrade-button {
    position: absolute; left: 90px; top: 1010px; width: 608px; height: 92px;
    border-radius: 16px;
    background: linear-gradient(180deg, var(--button-top) 0%, var(--button-bottom) 100%);
    box-shadow: 0 3px 6px rgba(0,0,0,0.25), inset 0 10px 8px -4px rgba(255,255,255,0.35);
    display: flex; align-items: center; justify-content: center;
    font-family: "Teko", sans-serif; font-weight: 500; color: var(--white);
    font-size: 50px; font-variant: small-caps; letter-spacing: 0.5px;
    padding-top: 8px; text-decoration: none;
  }
  .footnote {
    position: absolute; left: 454px; top: 1130px;
    font-family: "Ubuntu", sans-serif; font-size: 11px; color: var(--ink);
  }
</style>
</head>
<body>
<main class="banner">
  <div class="hero-photo" role="img" aria-label="Photo of a small tree in a white pot whose green foliage is shaped like a rising growth arrow, on a light grey tabletop"></div>

  <p class="lead headline">Are you ready to commit to</p>
  <h1 class="display display-business">TAKING YOUR BUSINESS</h1>
  <p class="lead lead-question">To the&nbsp; Next level?</p>
  <p class="lead lead-commit">Because we're in this for the<br>long-haul and dedicated</p>
  <h2 class="display display-success">To Your Success...</h2>

  <svg class="offer-disc" width="781" height="1200" viewBox="0 0 781 1200" aria-hidden="true">
    <circle cx="812" cy="716" r="292" fill="var(--ring)"/>
    <circle cx="818" cy="716" r="284" fill="var(--slate)"/>
  </svg>

  <div class="offer">
    <p class="offer-save">Save $300</p>
    <p class="offer-terms">By upgrading to an<br>Annual membership<br>and pay</p>
    <p class="offer-price">Only<br>$74/mth</p>
  </div>

  <a class="upgrade-button" href="https://tlpx.pagevault-example.com/page/tlp-annual-upsell">Yes, Upgrade My Plan Right Now!</a>
  <p class="footnote">*Must prepay the full year at only $898/yr!</p>
</main>
</body>
</html>
```